International Medical Company Needs a Website Design for a Support Site

We need a website design for a support site we are doing for ostomates called Bright Returns. We are an international company but this website is for our Australian market.

The website is a support site for people who are living with an Ostomy or Bowel Disease. This is a site where they can read other ostomates' stories and how they are dealing with the fact that they have to wear a pouch everyday.

The URL for our US site is: http://www.brightreturnsvale.com/

We need to use the same logo but we have freedom around the color scheme. We are not fond of the brown color scheme used in our US site and are happy for designs to be submitted with alternatives.

• We want the design to be clean, inspiring, modern and inviting.
• We would like to see a design for the mainpage / homepage and one of the subpages
• We only require the PSD / image files (no HTML needed)

Attached to this project is our sitemap, an example wireframe and the logos. We are happy for you to play around with different options and don't have to stick to the layout shown in the wireframe.

If you have any further questions please ask.

```html
<!DOCTYPE html>
<html lang="en">
<head>
<meta charset="utf-8">
<title>Bright Returns – Website Design</title>
<link href="https://fonts.googleapis.com/css2?family=Source+Sans+3:wght@400;600;700&display=swap" rel="stylesheet">
<style>
:root{
  --navy:#0b4f96;
  --bright:#0a86f2;
  --hero:#4d8fd8;
  --tab-grey:#d9dde2;
  --ink:#1a1a1a;
  --white:#ffffff;
  --stage-top:#ffffff;
  --stage-bottom:#d6d7d9;
}
*{box-sizing:border-box;margin:0;padding:0}
html,body{width:1200px;height:857px;overflow:hidden}
body{
  font-family:"Source Sans 3",sans-serif;
  background:radial-gradient(ellipse at 70% 40%,var(--stage-top) 40%,var(--stage-bottom) 100%);
  position:relative;color:var(--ink);
}
.page{position:absolute;background:var(--white);box-shadow:0 4px 14px rgba(0,0,0,.35);overflow:hidden;border:1px solid #c9c9c9}
.abs{position:absolute}
.brand{display:flex;align-items:center;gap:6px;font-size:17px;font-weight:600;color:var(--navy);letter-spacing:1px}
.brand-dot{width:10px;height:10px;border-radius:50%;background:var(--navy)}
.nav{display:flex;gap:11px;font-size:11.5px;font-weight:700;color:var(--navy);align-items:flex-end}
.nav .current{background:linear-gradient(#f2f3f5,#c7ccd3);color:#8aa4c4;padding:4px 8px 2px;border-radius:8px 8px 0 0}
.footer{position:absolute;left:0;right:0;bottom:0;height:32px;background:var(--navy)}
.footer-tab{position:absolute;left:0;top:0;height:14px;background:var(--white);border-radius:0 0 12px 0}
.footer-links{position:absolute;right:30px;bottom:6px;color:var(--white);font-size:11.5px}

/* back page */
.subpage{left:36px;top:259px;width:754px;height:566px}
.sidebar-head{background:linear-gradient(#fbfbfb,#c6cad0);color:var(--navy);font-weight:700;font-size:16px;text-align:center;height:30px;line-height:30px;border-radius:3px 3px 0 0}
.sidebar-block{background:var(--bright);color:var(--white)}
.story-list{list-style:none;padding:6px 4px}
.story-list li{font-weight:700;font-size:13px;padding:4px 20px;border-bottom:1px dashed rgba(255,255,255,.8)}
.story-list li:last-child{border-bottom:none}
.involved{font-size:11.3px;line-height:14px;padding:12px 18px;text-align:justify}
.video{background:#111;left:249px;top:89px;width:474px;height:285px}
.video-title{color:#ccc;font-size:11px;padding:4px 8px;height:22px;background:#2a2a2a}
.video-frame{position:absolute;left:0;top:22px;right:0;bottom:28px;background:linear-gradient(#b6c8d4 0%,#8ea4b2 45%,#5d6a6a 60%,#4a4a40 100%)}
.video-bar{position:absolute;left:0;right:0;bottom:0;height:28px;background:#1b1b1b;color:#ddd;font-size:9px}
.body-copy{font-size:11.2px;line-height:14.2px;text-align:justify}

/* front page */
.home{left:415px;top:21px;width:750px;height:565px}
.utility{left:411px;top:15px;width:340px;height:36px;background:var(--navy);border-radius:14px 0 0 14px;display:flex;align-items:center;gap:12px;padding-left:14px;color:var(--white);font-size:10.5px;font-weight:700}
.search{width:110px;height:18px;border-radius:9px;background:var(--white);color:#b0b0b0;font-size:10px;font-weight:400;text-align:center;line-height:18px}
.flag{width:16px;height:10px;background:repeating-linear-gradient(#c8202f 0 1.4px,#fff 1.4px 2.8px);position:relative}
.flag::before{content:"";position:absolute;left:0;top:0;width:7px;height:6px;background:#2b3f8c}
.hero{left:0;top:79px;width:750px;height:211px;background:var(--hero)}
.hero h1{position:absolute;left:62px;top:39px;font-size:21px;font-weight:400;color:var(--white)}
.hero p{position:absolute;left:62px;top:80px;width:311px;font-size:10.6px;line-height:13.4px;color:var(--white);text-align:justify}
.slide{position:absolute;left:402px;top:14px;width:285px;height:184px;border:3px solid var(--white);box-shadow:0 1px 4px rgba(0,0,0,.4);background:linear-gradient(135deg,#0c4f96,#1a5fa8)}
.slide-title{position:absolute;right:30px;top:16px;color:var(--white);font-weight:700;font-size:14px}
.slide-sub{position:absolute;left:58px;top:42px;color:var(--white);font-size:7.5px;font-style:italic}
.slide-photo{position:absolute;left:4px;top:64px;width:184px;height:108px;background:linear-gradient(90deg,#c9a89b,#e3cfc4 50%,#7b5a4a)}
.slide-brand{position:absolute;right:14px;top:150px;color:var(--white);font-size:8px;font-weight:700;letter-spacing:.5px;display:flex;gap:4px;align-items:center}
.slide-brand span{width:7px;height:7px;border-radius:50%;background:var(--white)}
.card{position:absolute;top:308px;width:223px;height:205px}
.card-head{height:40px;background:linear-gradient(#f7f7f7,#c9cdd3);color:var(--navy);font-weight:700;font-size:14.5px;padding:10px 14px 0}
.card-body{background:var(--bright);color:var(--white);height:165px;padding:10px 18px;font-size:11px;line-height:14.2px;text-align:justify}
</style>
</head>
<body>

<!-- Subpage: story -->
<section class="page subpage">
  <div class="abs brand" style="left:55px;top:64px">BRIGHTRETURNS<span class="brand-dot"></span></div>
  <nav class="abs nav" style="left:275px;top:62px"><span>HOME</span><span class="current">ABOUT</span><span>P</span></nav>

  <aside class="abs" style="left:18px;top:90px;width:203px">
    <div class="sidebar-head">FEATURED STORIES</div>
    <div class="sidebar-block" style="height:148px">
      <ul class="story-list">
        <li>Mara Ellison</li><li>Mara Ellison</li><li>Mara Ellison</li><li>Mara Ellison</li><li>Mara Ellison</li>
      </ul>
    </div>
    <div class="sidebar-head">GET INVOLVED</div>
    <div class="sidebar-block involved" style="height:231px">A unifying feeling for many people after ostomy surgery is that they can again lead a full and productive life. The Bright Returns® Program recognizes these inspirational individuals, both in their personal lives and in their contributions to their communities.</div>
  </aside>

  <div class="abs video">
    <div class="video-title">Bright Returns® Shining</div>
    <div class="video-frame" role="img" aria-label="Video still of a red kayak on a lake shore"></div>
    <div class="video-bar">
      <svg width="474" height="28" viewBox="0 0 474 28">
        <rect x="0" y="0" width="474" height="3" fill="#555"/><rect x="0" y="0" width="14" height="3" fill="#d22"/>
        <circle cx="14" cy="1.5" r="4" fill="#eee"/>
        <path d="M18 10 L26 15 L18 20Z" fill="#ccc"/>
        <path d="M45 12 h3 l4 -3 v12 l-4 -3 h-3z" fill="#ccc"/>
        <text x="70" y="19" fill="#ddd" font-size="9">0:09 / 7:43</text>
        <circle cx="420" cy="15" r="4" fill="none" stroke="#ccc" stroke-width="1.5"/>
        <rect x="440" y="10" width="10" height="10" fill="none" stroke="#ccc" stroke-width="1.5"/>
      </svg>
    </div>
  </div>

  <div class="abs body-copy" style="left:255px;top:380px;width:465px">
    <p>Lrem ipsum dolor sit amet, pri ut dico legimus eligendi, no quidam audire per. Expetenda iracundia accommodare ius at, mea ex facer ullamcorper. Ne his velit iudicabit reformidans, homero sanctus percipit sit et, labore luptatum voluptatibus no qui. Sit ex vocent reprehendunt comprehensam. Ea mollis civibus nam. Vim simul inciderint cu. No sea quas electram convenire, at duo nostrum dissentias honestatis, ad suas consulatu mnesarchum vis.</p>
    <p style="margin-top:14px">Lrem ipsum dolor sit amet, pri ut dico legimus eligendi, no quidam audire per. Expetenda iracundia accommodare ius at, mea ex facer ullamcorper. Ne his velit iudicabit reformidans, homero sanctus percipit sit et, labore luptatum voluptatibus no qui. Sit ex vocent reprehendunt comprehensam. Ea mollis civibus nam. Vim simul inciderint cu. No sea quas electram convenire, at duo nostrum dissentias honestatis, ad suas consulatu mnesarchum vis.</p>
  </div>

  <footer class="footer" style="height:18px">
    <div class="footer-tab" style="width:513px;height:0"></div>
    <div class="footer-links" style="right:32px;bottom:2px">Legal Notice | Privacy Policy | Site Map</div>
  </footer>
</section>

<!-- Homepage -->
<section class="page home">
  <div class="abs brand" style="left:46px;top:60px">BRIGHTRETURNS<span class="brand-dot"></span></div>
  <div class="abs utility"><div class="search">Search</div><span>SHARE A STORY</span><span>COUNTRY</span><div class="flag"></div></div>
  <nav class="abs nav" style="left:234px;top:58px">
    <span class="current">HOME</span><span>ABOUT</span><span>PERSONAL STORIES</span><span>TIPS FOR LIVING</span><span>NEWS</span><span>RESOURCES</span><span>CONTACTS</span>
  </nav>

  <div class="abs hero">
    <h1>Lrem ipsum dolor sit amet</h1>
    <p>Lrem ipsum dolor sit amet, pri ut dico legimus eligendi, no quidam audire per. Expetenda iracundia accommodare ius at, mea ex facer ullamcorper. Ne his velit iudicabit reformidans, homero sanctus percipit sit et, labore luptatum voluptatibus no qui. Sit ex vocent reprehendunt comprehensam. Ea mollis civibus nam. Vim simul inciderint cu. No sea quas electram convenire, at duo nostrum dissentias honestatis, ad suas consulatu mnesarchum vis.</p>
    <svg class="abs" style="left:380px;top:91px" width="30" height="26" viewBox="0 0 30 26"><path d="M0 13 L14 0 V7 H30 V19 H14 V26Z" fill="#3f73ad"/></svg>
    <svg class="abs" style="left:700px;top:91px" width="30" height="26" viewBox="0 0 30 26"><path d="M30 13 L16 0 V7 H0 V19 H16 V26Z" fill="#3f73ad"/></svg>
    <div class="slide">
      <div class="slide-title">The Voice of Inspiration.</div>
      <div class="slide-sub">Making a Difference.</div>
      <div class="slide-photo" role="img" aria-label="Photo of three smiling healthcare professionals"></div>
      <div class="slide-brand">BRIGHT RETURNS<span></span></div>
    </div>
  </div>

  <article class="card" style="left:36px"><div class="card-head">What is The Bright Returns?</div><div class="card-body">Lrem ipsum dolor sit amet, pri ut dico legimus eligendi, no quidam audire per. Expetenda iracundia accommodare ius at, mea ex facer ullamcorper. Ne his velit iudicabit reformidans, homero sanctus percipit sit et, labore luptatum voluptatibus no qui. Sit ex vocent reprehendunt comprehensam.</div></article>
  <article class="card" style="left:266px"><div class="card-head">Share A Story</div><div class="card-body">Lrem ipsum dolor sit amet, pri ut dico legimus eligendi, no quidam audire per. Expetenda iracundia accommodare ius at, mea ex facer ullamcorper. Ne his velit iudicabit reformidans, homero sanctus percipit sit et, labore luptatum voluptatibus no qui. Sit ex vocent reprehendunt comprehensam.</div></article>
  <article class="card" style="left:498px"><div class="card-head">News</div><div class="card-body">Lrem ipsum dolor sit amet, pri ut dico legimus eligendi, no quidam audire per. Expetenda iracundia accommodare ius at, mea ex facer ullamcorper. Ne his velit iudicabit reformidans, homero sanctus percipit sit et, labore luptatum voluptatibus no qui. Sit ex vocent reprehendunt comprehensam.</div></article>

  <footer class="footer">
    <div class="footer-tab" style="width:500px"></div>
    <div class="footer-links">Legal Notice | Privacy Policy | Site Map</div>
  </footer>
</section>

</body>
</html>
```